Business card design needed

I need a business card for my Sydney Painting Business, that specialises in painting High -end residential homes. i want the design to look clean, modern and edgy. i also want a logo next to the RK Decorating, using RKD together.

Industry/Entity Type

Residential

Contact Information for Business Card

RK Decorating (business name),LIC 581062B, Rob Kellaway, robert.kellaway@fernmail.net, mobile 0412573068

```html
<!DOCTYPE html>
<html lang="en">
<head>
<meta charset="utf-8">
<title>RK Decorating — Business Card</title>
<link rel="stylesheet" href="https://fonts.googleapis.com/css2?family=Cabin:wght@500;700&family=Arimo:wght@400&display=swap">
<style>
  :root {
    --page: #e9e6df;
    --card-white: #ffffff;
    --olive-dark: #6f7350;
    --olive-bright: #b3b134;
    --olive-text: #7a7a2e;
    --ink: #111111;
    --grey-text: #333333;
    --shadow: rgba(40, 35, 20, 0.22);
  }
  * { box-sizing: border-box; margin: 0; padding: 0; }
  html, body {
    width: 1200px;
    height: 892px;
    overflow: hidden;
    background: var(--page);
  }
  .sheet {
    position: relative;
    width: 1200px;
    height: 892px;
  }
  .card {
    position: absolute;
    width: 560px;
    height: 320px;
    border-radius: 26px;
    overflow: hidden;
    box-shadow: 0 8px 22px var(--shadow);
  }

  /* Front */
  .card-front {
    left: 90px;
    top: 100px;
    background: var(--card-white);
  }
  .brand {
    position: absolute;
    left: 40px;
    top: 44px;
    display: flex;
    align-items: center;
    gap: 12px;
  }
  .brand-mark {
    width: 26px;
    height: 26px;
    background: var(--olive-text);
  }
  .brand-name {
    font-family: "Cabin", sans-serif;
    font-weight: 700;
    font-size: 26px;
    color: var(--olive-text);
  }
  .identity {
    position: absolute;
    right: 40px;
    top: 40px;
    text-align: right;
  }
  .person-name {
    font-family: "Cabin", sans-serif;
    font-weight: 500;
    font-size: 24px;
    color: var(--olive-text);
  }
  .licence {
    margin-top: 6px;
    font-family: "Cabin", sans-serif;
    font-weight: 500;
    font-size: 16px;
    letter-spacing: 1.5px;
    color: var(--grey-text);
  }
  .contacts {
    position: absolute;
    left: 40px;
    top: 150px;
    list-style: none;
  }
  .contact {
    display: flex;
    align-items: center;
    gap: 10px;
    font-family: "Arimo", sans-serif;
    font-size: 15px;
    color: var(--ink);
    margin-bottom: 10px;
  }
  .contact-icon {
    width: 18px;
    height: 16px;
    flex: none;
  }
  .stripe {
    position: absolute;
    left: 0;
    width: 100%;
  }
  .stripe-band { top: 232px; height: 30px; background: var(--olive-dark); }
  .stripe-ink { top: 274px; height: 4px; background: var(--ink); }
  .stripe-olive { top: 284px; height: 6px; background: var(--olive-bright); }

  /* Back */
  .card-back {
    left: 550px;
    top: 470px;
    background: var(--olive-bright);
    display: flex;
    align-items: center;
    justify-content: center;
    gap: 14px;
  }
  .card-back .brand-mark { background: var(--card-white); width: 30px; height: 30px; }
  .card-back .brand-name { color: var(--card-white); font-size: 34px; }
</style>
</head>
<body>
<main class="sheet">
  <section class="card card-front" aria-label="Business card front">
    <div class="brand">
      <span class="brand-mark"></span>
      <span class="brand-name">RK Decorating</span>
    </div>
    <div class="identity">
      <p class="person-name">Rob Kellaway</p>
      <p class="licence">LIC 581062B</p>
    </div>
    <ul class="contacts">
      <li class="contact">
        <svg class="contact-icon" viewBox="0 0 18 16" aria-hidden="true">
          <rect x="1" y="2" width="16" height="12" fill="none" stroke="#7a7a2e" stroke-width="1.6"/>
          <path d="M1 2 L9 9 L17 2" fill="none" stroke="#7a7a2e" stroke-width="1.6"/>
        </svg>
        <span>robert.kellaway@fernmail.net</span>
      </li>
      <li class="contact">
        <svg class="contact-icon" viewBox="0 0 18 16" aria-hidden="true">
          <rect x="5" y="0.8" width="8" height="14.4" rx="1.5" fill="none" stroke="#7a7a2e" stroke-width="1.6"/>
          <circle cx="9" cy="12.4" r="1" fill="#7a7a2e"/>
        </svg>
        <span>0412573068</span>
      </li>
    </ul>
    <div class="stripe stripe-band"></div>
    <div class="stripe stripe-ink"></div>
    <div class="stripe stripe-olive"></div>
  </section>

  <section class="card card-back" aria-label="Business card back">
    <span class="brand-mark"></span>
    <span class="brand-name">RK Decorating</span>
  </section>
</main>
</body>
</html>
```